TomasTunes poster

We need a poster to promote my live music show for hotels, Im playing for tourists in hotels in Palma de Mallorca, Spain, I would like to see the url of my web site in the poster www.tomastunes.es, in the web site you can see some of my music, thx

```html
<!DOCTYPE html>
<html lang="en">
<head>
<meta charset="UTF-8">
<title>TomasTunes Live Poster</title>
<link href="https://fonts.googleapis.com/css2?family=Abril+Fatface&family=Yellowtail&family=Archivo:wght@400;600&display=swap" rel="stylesheet">
<style>
  :root {
    --sky: #22c6d3;
    --sea: #2fb3bd;
    --deck: #c9a27a;
    --night: #122325;
    --orange: #f07f1a;
    --ink: #101a1b;
    --white: #ffffff;
    --page: #e6e6e3;
  }
  * { margin: 0; padding: 0; box-sizing: border-box; }
  html, body { width: 1200px; height: 767px; overflow: hidden; background: var(--page); }
  .poster {
    position: absolute; left: 346px; top: 23px;
    width: 507px; height: 720px; overflow: hidden;
    background: var(--sky);
    font-family: "Archivo", Arial, sans-serif; color: var(--white);
  }
  .title {
    position: absolute; left: 0; right: 0; top: 26px;
    text-align: center; font-family: "Abril Fatface", Georgia, serif;
    font-size: 58px; letter-spacing: 1px; color: var(--ink); line-height: 1;
  }
  .photo { position: absolute; left: 0; top: 131px; width: 507px; height: 460px; }
  .bottom { position: absolute; left: 0; top: 500px; width: 507px; height: 220px; }
  .live {
    position: absolute; left: 44px; top: 572px;
    font-family: "Yellowtail", cursive; font-size: 78px; color: var(--orange); line-height: 1;
  }
  .date { position: absolute; color: var(--orange); text-align: center; line-height: 1; }
  .date .day { display: block; font-size: 23px; }
  .date .month { display: block; font-size: 12px; margin-top: 2px; }
  .venue { position: absolute; font-size: 8.5px; font-weight: 600; line-height: 1.3; text-transform: uppercase; }
  .venue .time { display: block; margin-top: 5px; font-size: 12.5px; font-weight: 400; text-transform: none; }
  .venue .time small { font-size: 7px; }
  .contact { position: absolute; top: 683px; font-size: 12px; }
  .contact .label { color: var(--orange); margin-right: 6px; }
  .brand {
    position: absolute; left: 408px; top: 660px; width: 80px;
    text-align: center; font-size: 12px; font-weight: 600; color: var(--white);
  }
  .brand .dot { display: block; width: 8px; height: 8px; border-radius: 50%; background: var(--white); margin: 0 auto 4px; }
</style>
</head>
<body>
  <div class="poster">
    <h1 class="title">TOMASTUNES</h1>

    <svg class="photo" viewBox="0 0 507 460" role="img" aria-label="Photo of a guitarist seated on a seaside hotel terrace at dusk, with microphone stands, amplifier and the harbour behind">
      <defs>
        <linearGradient id="scene" x1="0" y1="0" x2="0" y2="1">
          <stop offset="0" stop-color="#2d6b5a"/>
          <stop offset="0.2" stop-color="#4a8a86"/>
          <stop offset="0.35" stop-color="#2fb3bd"/>
          <stop offset="0.6" stop-color="#c9a27a"/>
          <stop offset="1" stop-color="#b7c4c2"/>
        </linearGradient>
      </defs>
      <rect width="507" height="460" fill="url(#scene)"/>
    </svg>

    <svg class="bottom" viewBox="0 0 507 220" preserveAspectRatio="none">
      <path d="M0 70 C 120 30, 300 40, 507 12 L507 220 L0 220 Z" fill="var(--night)"/>
    </svg>

    <div class="live">Live</div>

    <div class="date" style="left:152px; top:558px;"><span class="day">14</span><span class="month">JUN</span></div>
    <div class="venue" style="left:198px; top:562px;">
      Harbor Groove 12 34 56 Sea View Street<br>Number 21.09 - Bay Front
      <span class="time">Starts at &nbsp; 08.00 <small>PM</small></span>
    </div>

    <div class="date" style="left:193px; top:617px;"><span class="day">14</span><span class="month">JUN</span></div>
    <div class="venue" style="left:238px; top:621px;">
      Harbor Groove 12 34 56 Sea View Street<br>Number 21.09 - Bay Front
      <span class="time">Starts at &nbsp; 08.00 <small>PM</small></span>
    </div>

    <div class="contact" style="left:46px;"><span class="label">website</span>www.tomastunes.es</div>
    <div class="contact" style="left:232px;"><span class="label">mail</span>marco@tomastunes.es</div>

    <div class="brand"><span class="dot"></span>TomasTunes</div>
  </div>
</body>
</html>
```